Refined Sweets Table & Vessel Rental Needs a logo & business card design

I need a logo design and a business card design for a new candy buffet company based in Melbourne called "Brightwater Table Co."(but the & Jar Hire part to be in smaller font). We set up candy bars with a wide variety of custom themes or to the customer's preference, we also hire out the glass jars if the customer prefers to do it themselves. But i want the emphasis on the front of the business card to be about the Candy Buffet and the jar hire can be at the back of the card. I would like to see designs that use the tiffany blue, or black and gold. I would like to see elegance, class but quite simple.

Industry/Entity Type

Business

Font styles to use
Script

```html
<!DOCTYPE html>
<html lang="en">
<head>
<meta charset="utf-8">
<title>Brightwater Table Co. – Business Card</title>
<link rel="stylesheet" href="https://fonts.googleapis.com/css2?family=Raleway:wght@300;400&display=swap">
<style>
  :root {
    --backdrop: #e9e6e1;
    --card-white: #ffffff;
    --tiffany: #3fb8b5;
    --tiffany-deep: #2ea3a0;
    --gold: #e3b52a;
    --ink-black: #0a0a0a;
    --text-light: #ffffff;
  }
  * { box-sizing: border-box; margin: 0; padding: 0; }
  html, body { width: 1200px; height: 783px; overflow: hidden; }
  body {
    background: var(--backdrop);
    display: flex;
    align-items: center;
    justify-content: center;
    gap: 60px;
    font-family: "Raleway", sans-serif;
  }
  .card {
    position: relative;
    width: 500px;
    height: 286px;
    border-radius: 4px;
    overflow: hidden;
    box-shadow: 0 8px 24px rgba(0,0,0,0.18);
  }

  /* Front */
  .card--front { background: var(--card-white); }
  .front-band {
    position: absolute;
    inset: 0;
    width: 100%;
    height: 100%;
  }
  .brand {
    position: absolute;
    display: flex;
    align-items: center;
    gap: 10px;
    color: var(--gold);
    font-family: "Raleway", sans-serif;
    font-weight: 400;
    white-space: nowrap;
  }
  .brand__mark {
    flex: none;
    border: 2px solid var(--gold);
    border-radius: 3px;
  }
  .card--front .brand { left: 22px; top: 24px; font-size: 20px; }
  .card--front .brand__mark { width: 22px; height: 22px; }

  .contact {
    position: absolute;
    left: 26px;
    top: 130px;
    color: var(--text-light);
  }
  .contact__name {
    font-weight: 300;
    font-size: 26px;
    letter-spacing: 0.5px;
    margin-bottom: 12px;
  }
  .contact__list { list-style: none; }
  .contact__item {
    display: flex;
    align-items: center;
    gap: 10px;
    font-size: 11.5px;
    font-weight: 300;
    line-height: 1;
    margin-bottom: 9px;
  }
  .contact__icon {
    width: 14px;
    height: 14px;
    flex: none;
    fill: var(--text-light);
  }

  /* Back */
  .card--back {
    background: var(--ink-black);
    display: flex;
    align-items: center;
    justify-content: center;
  }
  .card--back .brand {
    position: static;
    flex-direction: column;
    gap: 18px;
    font-size: 30px;
  }
  .card--back .brand__mark { width: 48px; height: 48px; border-width: 3px; }
</style>
</head>
<body>

  <section class="card card--front" aria-label="Business card front">
    <svg class="front-band" viewBox="0 0 500 286" aria-hidden="true" preserveAspectRatio="none">
      <path d="M0 110 C 150 100, 250 95, 300 70 C 330 55, 350 20, 350 0 L 500 0 L 500 286 L 0 286 Z" fill="var(--tiffany)"/>
      <path d="M300 70 C 330 55, 350 20, 350 0 L 370 0 C 370 25, 345 65, 300 80 Z" fill="var(--tiffany-deep)" opacity="0.5"/>
    </svg>

    <div class="brand">
      <span class="brand__mark"></span>
      <span class="brand__name">Brightwater Table Co.</span>
    </div>

    <div class="contact">
      <p class="contact__name">Marion Vale</p>
      <ul class="contact__list">
        <li class="contact__item">
          <svg class="contact__icon" viewBox="0 0 16 16"><path d="M8 1a5 5 0 0 0-5 5c0 4 5 9 5 9s5-5 5-9a5 5 0 0 0-5-5zm0 7a2 2 0 1 1 0-4 2 2 0 0 1 0 4z"/></svg>
          Fitzroy St, 18 b L 4
        </li>
        <li class="contact__item">
          <svg class="contact__icon" viewBox="0 0 16 16"><path d="M4 1l2 3-1.5 1.5c.8 2 2.5 3.7 4.5 4.5L10.5 8.5l3 2-1 3c-5.5 0-10-4.5-10-10z"/></svg>
          480 217 903
        </li>
        <li class="contact__item">
          <svg class="contact__icon" viewBox="0 0 16 16"><path d="M1 3h14v10H1z" fill="none" stroke="#fff" stroke-width="1.4"/><path d="M1 3l7 6 7-6" fill="none" stroke="#fff" stroke-width="1.4"/></svg>
          hello@brightwater.net
        </li>
        <li class="contact__item">
          <svg class="contact__icon" viewBox="0 0 16 16"><rect x="1" y="1" width="14" height="14" rx="2"/></svg>
          @brightwaterco
        </li>
      </ul>
    </div>
  </section>

  <section class="card card--back" aria-label="Business card back">
    <div class="brand">
      <span class="brand__mark"></span>
      <span class="brand__name">Brightwater Table Co.</span>
    </div>
  </section>

</body>
</html>
```